Accounting business needs business card

I have a business card but need something better. I want the colour changed and the design to be better. I have uploaded a picture of my new sign that is grey in colour, i would like to incorporate these colours.

```html
<!DOCTYPE html>
<html lang="en">
<head>
<meta charset="utf-8">
<title>Level Tax – Business Card</title>
<link href="https://fonts.googleapis.com/css2?family=Poppins:wght@400;500;600&display=swap" rel="stylesheet">
<style>
  :root {
    --backdrop: #2b2b2d;
    --card-white: #ffffff;
    --card-grey: #dedede;
    --ink: #2a2d31;
    --teal: #27b896;
    --icon-grey: #b9b9b9;
    --badge-lime: #c8d43a;
    --badge-blue: #1f56a3;
    --badge-yellow: #f3c51b;
    --badge-sky: #21b2e8;
  }
  html, body {
    margin: 0;
    padding: 0;
    width: 1200px;
    height: 880px;
    overflow: hidden;
    background: var(--backdrop);
    font-family: "Poppins", sans-serif;
  }
  .canvas {
    position: relative;
    width: 1200px;
    height: 880px;
  }
  .card {
    position: absolute;
    width: 620px;
    height: 355px;
    border-radius: 22px;
    overflow: hidden;
    box-shadow: 0 14px 30px rgba(0,0,0,0.45);
  }
  .card--back { left: 60px; top: 70px; background: var(--card-grey); }
  .card--front { left: 520px; top: 455px; background: var(--card-white); }
  .card svg { display: block; }
  .brand-name { font-family: "Poppins", sans-serif; font-weight: 500; fill: var(--ink); }
  .person-name { font-family: "Poppins", sans-serif; font-weight: 600; fill: var(--teal); }
  .person-line { font-family: "Poppins", sans-serif; font-weight: 400; fill: var(--ink); }
  .contact-line { font-family: "Poppins", sans-serif; font-weight: 400; fill: #ffffff; }
  .agent-note { font-family: "Poppins", sans-serif; font-weight: 400; fill: var(--ink); }
</style>
</head>
<body>
<main class="canvas">

  <!-- Card back -->
  <section class="card card--back" aria-label="Card back">
    <svg width="620" height="355" viewBox="0 0 620 355">
      <g class="social-links">
        <circle cx="48" cy="62" r="13" fill="var(--icon-grey)"/>
        <circle cx="84" cy="54" r="13" fill="var(--icon-grey)"/>
        <circle cx="120" cy="46" r="13" fill="var(--icon-grey)"/>
      </g>
      <circle class="brand-mark" cx="310" cy="125" r="52" fill="none" stroke="var(--ink)" stroke-width="3"/>
      <text class="brand-name" x="310" y="240" text-anchor="middle" font-size="40" letter-spacing="14">LEVEL TAX</text>
    </svg>
  </section>

  <!-- Card front -->
  <section class="card card--front" aria-label="Card front">
    <svg width="620" height="355" viewBox="0 0 620 355">
      <path class="wave-dark" d="M0 292 C 200 305, 320 270, 385 150 C 340 262, 230 318, 0 312 Z" fill="var(--ink)"/>
      <path class="wave-teal" d="M0 332 C 170 332, 300 330, 355 225 C 410 125, 480 140, 620 128 L620 355 L0 355 Z" fill="var(--teal)"/>

      <circle class="brand-mark" cx="160" cy="125" r="46" fill="none" stroke="var(--ink)" stroke-width="3"/>
      <text class="brand-name" x="160" y="225" text-anchor="middle" font-size="32" letter-spacing="11">LEVEL TAX</text>

      <text class="person-name" x="590" y="58" text-anchor="end" font-size="28">Owen Marsh</text>
      <text class="person-line" x="590" y="84" text-anchor="end" font-size="13">CAP, MTAX, BCOM (Acc &amp; Fin)</text>
      <text class="person-line" x="590" y="106" text-anchor="end" font-size="14">Taxation and Business Accountant</text>

      <g class="contact-list">
        <text class="contact-line" x="562" y="175" text-anchor="end" font-size="15">0400 555 018</text>
        <text class="contact-line" x="562" y="200" text-anchor="end" font-size="15">owen@leveltax.com.au</text>
        <text class="contact-line" x="562" y="225" text-anchor="end" font-size="15">www.leveltax.com.au</text>

        <g class="icon icon-phone">
          <circle cx="584" cy="170" r="9" fill="#ffffff"/>
          <path d="M579.5 166 q1.5-1.5 2.5 0 l1 2 q-1 1 0 2.5 q1.5 1.5 2.5 0.5 l2 1 q1.5 1 0 2.5 q-3 2-6.5-1.5 q-3.5-3.5-1.5-7 z" fill="var(--teal)"/>
        </g>
        <g class="icon icon-mail">
          <circle cx="584" cy="195" r="9" fill="#ffffff"/>
          <rect x="578.5" y="191" width="11" height="8" fill="none" stroke="var(--teal)" stroke-width="1.4"/>
          <path d="M578.5 191 l5.5 4.5 l5.5 -4.5" fill="none" stroke="var(--teal)" stroke-width="1.4"/>
        </g>
        <g class="icon icon-web">
          <circle cx="584" cy="220" r="9" fill="#ffffff"/>
          <circle cx="584" cy="220" r="5.5" fill="none" stroke="var(--teal)" stroke-width="1.3"/>
          <path d="M578.5 220 h11 M584 214.5 v11" stroke="var(--teal)" stroke-width="1.1"/>
        </g>
      </g>

      <g class="badges">
        <circle class="badge-board" cx="395" cy="292" r="26" fill="var(--badge-lime)" stroke="#ffffff" stroke-width="3"/>
        <text class="agent-note" x="395" y="333" text-anchor="middle" font-size="8">Tax agent 10203040</text>
        <rect class="badge-body" x="445" y="272" width="68" height="40" fill="var(--badge-blue)"/>
        <rect class="badge-body-end" x="513" y="272" width="26" height="40" fill="var(--badge-yellow)"/>
        <circle class="badge-software" cx="578" cy="270" r="27" fill="var(--badge-sky)"/>
      </g>
    </svg>
  </section>

</main>
</body>
</html>
```